Postcard Design

I'm hosting a retreat in Tuscany tag line ideas for front: "nourish your soul with a taste of Tuscany" or "Savor the sweet life and Nourish your soul with a taste of Tuscany" here is the pertinent info- trip date: September 5-12, 2015 number:1.877.384.2951 e/m:Info@WillowmereRetreats.example Web address:www.WillowmereRetreats.example
What's included:
• 7 nights Accommodations in beautiful Villa
• All Meals and Snacks included
• Special Wine tasting Excursion in Chianti
• Guided Tour of Siena
• Hands on Cooking Class at the villa
• Yoga, Meditation walks, Journaling
Something like this should be on back lower right side: Spaces Limited Reserve Yours Today!
Other wording ideas for back: Renew your spirit in the quiet beauty of the Tuscan landscape (maybe above what's included)
This can be near the "spaces limited" =Invest in your health, spirit and well-being *airfare not included. See website for details
More ideas/maybe a better way to word all this??:
Welcome to "la dolce vita" (The sweet life)
Have you always wanted to travel to Italy? Want to experience the culture in a special way you couldn't enjoy as a typical tourist? This is the trip you've been waiting for. Life is too short to wait any longer!
Hosts show with pictures:
Lise Karen Bouchard woman w/dark hair headshot
Retreat host
Sharing her love of Italy's beautiful culture with you is her special gift
And
Greta Halvorsen
Personal wellness consultant
Yoga, Meditation, Asana, Reiki, Pilates

I included a photo of the current postcard I made front & back. You can also visit my website to get an idea of my style. I'm hoping you can make me a postcard that's more tantalizing, and will get me some clients! I will include some extra photos and feel free to use your own stock images... anything to help! Feel free to change up wording to make it more appealing, welcoming and make people chose to go on retreat with me instead the hundreds of other retreats out there.
Thank you
Lise Karen

```html
<!DOCTYPE html>
<html lang="en">
<head>
<meta charset="utf-8">
<title>Willowmere Wellness Retreat – Postcard</title>
<link rel="stylesheet" href="https://fonts.googleapis.com/css2?family=Kalam:wght@400;700&family=Varela+Round&family=Cormorant+SC:wght@600&display=swap">
<style>
  :root {
    --page: #ece6de;
    --orange-light: #f4a650;
    --orange: #e8832a;
    --orange-deep: #d8691c;
    --brown: #7a3712;
    --cream: #fff4e2;
    --peach: #f8d7b4;
    --white: #ffffff;
    --sun: #f7c531;
    --sun-deep: #eea81c;
    --green-light: #a6d46a;
    --green: #4f8f2c;
    --sky: #9cc6ea;
    --ink: #5a2a0e;
  }
  * { box-sizing: border-box; margin: 0; padding: 0; }
  html, body { width: 1200px; height: 800px; overflow: hidden; background: var(--page); }
  .canvas { position: relative; width: 1200px; height: 800px; }
  .card {
    position: absolute; top: 205px; width: 570px; height: 390px;
    background: var(--white); overflow: hidden;
    box-shadow: 0 6px 18px rgba(60, 35, 15, .25);
  }
  .card--back { left: 20px; }
  .card--front { left: 610px; }
  .script { font-family: "Kalam", cursive; }
  .sans { font-family: "Varela Round", sans-serif; }
  .abs { position: absolute; }

  /* Back: hosts column */
  .hosts { left: 0; top: 0; width: 230px; height: 390px; }
  .hosts__petals {
    left: 20px; top: 0; width: 190px; height: 52px;
    background: radial-gradient(ellipse at 50% 60%, #fbe27a 0%, #fdf0b6 55%, rgba(255,255,255,0) 75%);
  }
  .hosts__title { left: 0; width: 230px; top: 6px; text-align: center; font-size: 26px; font-weight: 700; color: var(--brown); }
  .host-photo { top: 50px; width: 106px; height: 166px; }
  .host-photo--one { left: 6px; background: linear-gradient(170deg, #8a9a6a, #5a4a3a 55%, #e8e0d8); }
  .host-photo--two { left: 118px; background: linear-gradient(180deg, #d9d6d0, #9a928a 55%, #5e4a3a); }
  .host-sun {
    left: 40px; top: 236px; width: 140px; height: 64px;
    background: radial-gradient(ellipse at 50% 50%, #fbe89a 0%, rgba(255,255,255,0) 70%);
  }
  .host-info { top: 220px; width: 112px; text-align: center; color: var(--brown); }
  .host-info--one { left: 2px; }
  .host-info--two { left: 116px; }
  .host-info__name { font-family: "Cormorant SC", serif; font-weight: 600; font-size: 11.5px; line-height: 1.1; }
  .host-info__role { font-family: "Cormorant SC", serif; font-weight: 600; font-size: 9.5px; margin-top: 1px; }
  .host-info__note { font-family: "Kalam", cursive; font-size: 9px; line-height: 1.25; color: var(--orange-deep); margin-top: 8px; }
  .reserve {
    left: 0; top: 300px; width: 230px; height: 90px;
    background: linear-gradient(180deg, var(--peach), #fbe8d4);
  }
  .reserve__line { width: 230px; text-align: center; color: var(--ink); font-size: 16px; line-height: 1.15; }
  .reserve__text { top: 8px; }
  .reserve__mail { left: 14px; top: 64px; display: flex; align-items: center; gap: 6px; font-size: 11.5px; color: var(--orange-deep); }

  /* Back: offer column */
  .offer {
    left: 230px; top: 0; width: 340px; height: 300px;
    background: linear-gradient(180deg, var(--orange) 0%, var(--orange-light) 100%);
  }
  .offer__lead { left: 0; width: 340px; top: 8px; text-align: center; font-size: 16.5px; line-height: 1.35; color: var(--cream); }
  .offer__list { left: 18px; top: 70px; list-style: none; }
  .offer__item { display: flex; gap: 8px; color: var(--white); font-size: 13.5px; line-height: 1.15; margin-bottom: 8px; }
  .offer__item svg { flex: none; margin-top: 2px; }
  .offer__tagline { left: 12px; top: 266px; font-size: 15px; font-weight: 700; color: var(--brown); white-space: nowrap; }
  .landscape {
    left: 230px; top: 300px; width: 340px; height: 90px;
    background: linear-gradient(180deg, #cfe6c0 0%, var(--green-light) 40%, var(--green) 100%);
  }
  .landscape__brand { right: 18px; top: 14px; text-align: right; color: var(--white); font-size: 17px; line-height: 1; }

  /* Front */
  .villa {
    left: 0; top: 0; width: 320px; height: 250px;
    background: linear-gradient(180deg, var(--sky) 0%, #d8e6ee 35%, #c99b6a 55%, var(--green) 85%, #3f7a25 100%);
  }
  .quote-band {
    left: 0; top: 16px; width: 320px; height: 42px;
    background: linear-gradient(90deg, rgba(255,255,255,.55), rgba(255,255,255,.15));
  }
  .quote-band__text { left: 0; width: 320px; top: 8px; text-align: center; font-size: 14px; color: var(--brown); }
  .quote-band__rule { left: 40px; top: 50px; width: 240px; height: 1px; background: var(--orange-deep); }
  .sunflower {
    left: 28px; top: 162px; width: 108px; height: 108px; border-radius: 50%;
    background: linear-gradient(160deg, var(--sun) 0%, var(--sun-deep) 100%);
  }
  .details { left: 18px; top: 282px; width: 262px; color: var(--orange-deep); }
  .details__date { font-size: 24px; line-height: 1; white-space: nowrap; }
  .details__rule { width: 250px; height: 1px; background: var(--orange-deep); margin: 7px 0 7px; }
  .details__web { font-size: 14.5px; white-space: nowrap; }
  .details__phone { display: flex; align-items: center; gap: 8px; font-size: 14px; margin-top: 9px; }
  .brand-panel {
    left: 320px; top: 0; width: 250px; height: 255px;
    background: linear-gradient(180deg, var(--orange-deep) 0%, var(--orange) 50%, var(--orange-light) 100%);
  }
  .brand-panel__petals {
    left: 10px; top: 0; width: 230px; height: 150px;
    background: radial-gradient(ellipse at 50% 40%, rgba(250,205,80,.65) 0%, rgba(240,150,40,0) 70%);
  }
  .brand-panel__name { left: 0; width: 250px; top: 46px; text-align: center; color: var(--cream); font-size: 28px; line-height: 1.05; }
  .brand-panel__rule { left: 40px; top: 130px; width: 170px; height: 1px; background: var(--cream); }
  .brand-panel__tagline { left: 0; width: 250px; top: 150px; text-align: center; color: var(--brown); font-size: 15px; line-height: 1.25; }
  .brand-panel__place { display: block; font-size: 24px; font-weight: 700; }
  .yoga {
    left: 290px; top: 255px; width: 280px; height: 135px;
    background: linear-gradient(180deg, #b9cf9a 0%, #8fb566 45%, #5f9a35 100%);
  }
</style>
</head>
<body>
<main class="canvas">

  <section class="card card--back" aria-label="Postcard back">
    <div class="abs hosts">
      <div class="abs hosts__petals" role="img" aria-label="Sunflower petals behind the heading"></div>
      <h2 class="abs hosts__title script">Your Hosts:</h2>
      <div class="abs host-photo host-photo--one" role="img" aria-label="Portrait photo of Lise Karen Bouchard"></div>
      <div class="abs host-photo host-photo--two" role="img" aria-label="Photo of Greta Halvorsen in a yoga tree pose on rocks"></div>
      <div class="abs host-sun" role="img" aria-label="Faint sunflower decoration"></div>
      <div class="abs host-info host-info--one">
        <p class="host-info__name">Lise Karen Bouchard</p>
        <p class="host-info__role">Retreat Host</p>
        <p class="host-info__note">Sharing her love of Italy's beautiful culture with you is her special gift</p>
      </div>
      <div class="abs host-info host-info--two">
        <p class="host-info__name">Greta Halvorsen</p>
        <p class="host-info__role">Personal Wellness Consultant</p>
        <p class="host-info__note">Yoga, Meditation, Asana, Reiki, Pilates</p>
      </div>
      <div class="abs reserve">
        <p class="abs reserve__line reserve__text sans">Spaces limited<br>Reserve yours TODAY!</p>
        <p class="abs reserve__mail sans">
          <svg width="16" height="12" viewBox="0 0 16 12" aria-hidden="true"><rect x="1" y="1" width="14" height="10" fill="none" stroke="#d8691c" stroke-width="1.4"/><path d="M1 1 L8 7 L15 1" fill="none" stroke="#d8691c" stroke-width="1.4"/></svg>
          Info@WillowmereRetreats.example
        </p>
      </div>
    </div>

    <div class="abs offer">
      <p class="abs offer__lead script">Renew your spirit in the quiet beauty<br>of the Tuscan landscape</p>
      <ul class="abs offer__list sans">
        <li class="offer__item"><svg width="18" height="12" viewBox="0 0 18 12" aria-hidden="true"><path d="M2 6 C5 1 9 1 9 6 C9 11 13 11 16 6" fill="none" stroke="#fff4e2" stroke-width="1.6"/></svg><span>7 nights Accommodations in<br>beautiful Villa</span></li>
        <li class="offer__item"><svg width="18" height="12" viewBox="0 0 18 12" aria-hidden="true"><path d="M2 6 C5 1 9 1 9 6 C9 11 13 11 16 6" fill="none" stroke="#fff4e2" stroke-width="1.6"/></svg><span>All Meals and Snacks included</span></li>
        <li class="offer__item"><svg width="18" height="12" viewBox="0 0 18 12" aria-hidden="true"><path d="M2 6 C5 1 9 1 9 6 C9 11 13 11 16 6" fill="none" stroke="#fff4e2" stroke-width="1.6"/></svg><span>Special Wine tasting Excursion<br>in Chianti</span></li>
        <li class="offer__item"><svg width="18" height="12" viewBox="0 0 18 12" aria-hidden="true"><path d="M2 6 C5 1 9 1 9 6 C9 11 13 11 16 6" fill="none" stroke="#fff4e2" stroke-width="1.6"/></svg><span>Tour medieval city of Siena</span></li>
        <li class="offer__item"><svg width="18" height="12" viewBox="0 0 18 12" aria-hidden="true"><path d="M2 6 C5 1 9 1 9 6 C9 11 13 11 16 6" fill="none" stroke="#fff4e2" stroke-width="1.6"/></svg><span>Hands on Cooking Class</span></li>
        <li class="offer__item"><svg width="18" height="12" viewBox="0 0 18 12" aria-hidden="true"><path d="M2 6 C5 1 9 1 9 6 C9 11 13 11 16 6" fill="none" stroke="#fff4e2" stroke-width="1.6"/></svg><span>Yoga, Meditation walks, Journaling</span></li>
      </ul>
      <p class="abs offer__tagline script">Invest in your health, spirit and well-being</p>
    </div>

    <div class="abs landscape" role="img" aria-label="Rolling green Tuscan hills with a cypress-lined farmhouse and a woman meditating">
      <p class="abs landscape__brand script">Willowmere Wellness Retreat</p>
    </div>
  </section>

  <section class="card card--front" aria-label="Postcard front">
    <div class="abs villa" role="img" aria-label="Stone Tuscan villa with a pool among green fields under a blue sky"></div>
    <div class="abs quote-band">
      <p class="abs quote-band__text script">To travel is to take a journey into yourself</p>
      <div class="abs quote-band__rule"></div>
    </div>

    <div class="abs brand-panel">
      <div class="abs brand-panel__petals" role="img" aria-label="Large sunflower head behind the retreat name"></div>
      <p class="abs brand-panel__name script">Willowmere<br>Wellness Retreat</p>
      <div class="abs brand-panel__rule"></div>
      <p class="abs brand-panel__tagline script">Savor the sweet life and<br>Nourish your soul with a taste of
        <span class="brand-panel__place">Tuscany</span></p>
    </div>

    <div class="abs yoga" role="img" aria-label="Woman in a yoga pose with arms raised on a green lawn"></div>
    <div class="abs sunflower" role="img" aria-label="Sunflower bloom"></div>

    <div class="abs details sans">
      <p class="details__date">September 5-12 2015</p>
      <div class="details__rule"></div>
      <p class="details__web">www.WillowmereRetreats.example</p>
      <p class="details__phone">
        <svg width="18" height="18" viewBox="0 0 18 18" aria-hidden="true"><rect width="18" height="18" rx="4" fill="#e8832a"/><path d="M5 4 L7.5 4 L8.5 6.5 L7 7.5 C7.6 9 9 10.4 10.5 11 L11.5 9.5 L14 10.5 L14 13 C9 13.5 4.5 9 5 4 Z" fill="#fff"/></svg>
        1.877.384.2951
      </p>
    </div>
  </section>

</main>
</body>
</html>
```